Brackenfold Lane Vineyard website

I need to have our website design done. It is an existing site www.brackenfoldlane.com.au which is based on Wordpress which includes information and online purchasing of our wine. Logo and existing branding are to be maintained but website needs to be improved and open to recommendations for function extensions.

Target Market(s)

Wine drinkers and people wanting to visit or hold and event.
Aged from 25-55, men and women

Industry/Entity Type

Vineyard

Number of Pages Required

5+ page

Font styles to use
Sans Serif

Requirements
Must have
• Incorporate existing logos and styling from bottles.
• See existing website www.brackenfoldlane.com.au

```html
<!DOCTYPE html>
<html lang="en">
<head>
<meta charset="utf-8">
<title>Brackenfold Lane Vineyard</title>
<link href="https://fonts.googleapis.com/css2?family=Cinzel:wght@400;700&family=Open+Sans:wght@400;600;700&display=swap" rel="stylesheet">
<style>
:root{
  --green:#1e9a33;
  --green-dark:#15802a;
  --ink:#2b2b2b;
  --text:#555;
  --muted:#888;
  --line:#dcdcdc;
  --panel:#f4f4f4;
  --nav:#3a3a3a;
  --footer:#000;
  --field:#2e2e2e;
}
*{box-sizing:border-box;margin:0;padding:0}
html,body{width:1200px;height:2261px;overflow:hidden;background:#fff}
body{position:relative;font-family:"Open Sans",Arial,sans-serif;color:var(--text)}
.abs{position:absolute}
.serif{font-family:"Cinzel",Georgia,serif}

/* header */
.topline{left:0;top:0;width:1200px;height:3px;background:var(--green)}
.brand{left:85px;top:30px;width:220px;text-align:center;color:var(--ink);white-space:nowrap}
.brand-mark{width:16px;height:16px;border-radius:50%;background:var(--ink);margin:0 auto 8px}
.brand-name{font-size:16px;letter-spacing:.3px;line-height:1.2}
.brand-sub{font-size:9px;letter-spacing:1px}
.callus{left:614px;top:48px;display:flex;align-items:center;gap:8px;white-space:nowrap}
.callus .lbl{font-size:12px;color:var(--text);line-height:1}
.callus .num{font-size:17px;color:var(--green);line-height:1.2}
.search{left:814px;top:46px;width:286px;height:40px;display:flex;border:1px solid var(--line)}
.search span{flex:1;font-size:12px;color:var(--muted);padding:11px 12px}
.search b{width:40px;background:var(--green);display:flex;align-items:center;justify-content:center}

/* nav */
.nav{left:0;top:130px;width:1200px;height:53px;background:linear-gradient(#444,#2c2c2c)}
.nav a{position:absolute;top:0;height:53px;line-height:53px;font-family:"Cinzel",Georgia,serif;font-size:13px;color:#fff;text-decoration:none;text-align:center;transform:translateX(-50%);white-space:nowrap}
.nav .home{left:158px;width:116px;background:var(--green)}
.nav .sep{position:absolute;top:10px;width:1px;height:33px;background:#555}

/* hero */
.hero{left:0;top:183px;width:1200px;height:456px;background:linear-gradient(100deg,#3a1f1c 0%,#7a3f2a 25%,#c9792e 50%,#9b5a2a 75%,#4a2b1c 100%)}
.hero-title{left:0;top:342px;width:1242px;text-align:center;font-size:29px;color:#fff;letter-spacing:1px;white-space:nowrap}
.hero-text{left:370px;top:384px;width:500px;text-align:center;font-size:15px;line-height:22px;color:#fff}
.btn-solid{background:var(--green);color:#fff;text-align:center;border-radius:2px;font-size:15px}
.hero-btn{left:555px;top:440px;width:131px;height:44px;line-height:44px}
.arrow{top:410px}

/* features */
.feature{top:639px;width:318px;height:291px;background:#fff;box-shadow:0 6px 10px rgba(0,0,0,.12);border:1px solid #eee;text-align:center}
.feature .circle{position:absolute;left:82px;top:-83px;width:154px;height:154px;border-radius:50%;background:#fff;box-shadow:0 0 6px rgba(0,0,0,.15);display:flex;align-items:center;justify-content:center}
.feature h3{position:absolute;top:78px;width:100%;font-weight:400;font-size:20px;color:var(--ink);letter-spacing:1px;white-space:nowrap}
.feature p{position:absolute;top:109px;left:30px;width:258px;font-size:12px;line-height:22px;color:#555}
.btn-line{position:absolute;left:94px;top:204px;width:129px;height:42px;line-height:40px;border:1.5px solid var(--green);color:var(--green);font-size:15px}

/* products */
.products{left:0;top:987px;width:1200px;height:558px;background:var(--panel);border-top:1px solid #e6e6e6}
.sec-title{display:inline-block;white-space:nowrap;font-size:30px;color:var(--ink);letter-spacing:1px;line-height:1.2}
.sec-title::after{content:"";display:block;height:2px;background:var(--ink);margin-top:2px}
.prod-head{left:0;top:1028px;width:1356px;text-align:center}
.card{top:1095px;width:238px;height:383px;background:#eee;border:1px solid #ddd}
.card .img{position:absolute;left:4px;top:4px;width:228px;height:251px;background:#faf8f8;border:1px solid #e6e6e6}
.card .bottle{position:absolute;left:99px;top:26px;width:30px;height:200px;border-radius:8px 8px 4px 4px}
.card h4{position:absolute;top:272px;width:100%;text-align:center;font-weight:400;font-size:14px;color:#444;white-space:nowrap}
.card .price{position:absolute;top:296px;width:100%;text-align:center;font-weight:700;font-size:15px;color:var(--green)}
.card .row{position:absolute;left:0;top:327px;width:236px;height:54px;border-top:1px solid #ddd}
.qty{position:absolute;left:19px;top:13px;width:42px;height:28px;background:#fff;font-size:13px;padding:5px 9px;color:#555}
.add{position:absolute;left:130px;top:12px;width:88px;height:30px;line-height:27px;text-align:center;border:1.5px solid var(--green);color:var(--green);background:#fff;font-size:14px}
.sale{position:absolute;left:168px;top:8px;width:58px;height:58px;border-radius:50%;background:var(--green);border:3px solid #fff;color:#fff;font-size:14px;text-align:center;line-height:52px}

/* about */
.about-photo{left:98px;top:1593px;width:365px;height:304px;border:5px solid #fff;box-shadow:0 0 5px rgba(0,0,0,.3);background:linear-gradient(160deg,#d9d6d2,#8a8482 55%,#5a4a44)}
.about-head{left:491px;top:1582px}
.about-list{left:491px;top:1642px;width:610px;list-style:none;font-size:12px;line-height:21px;color:#444}
.about-list li{position:relative;padding-left:24px;margin-bottom:4px}
.about-list li::before{content:"";position:absolute;left:3px;top:6px;width:8px;height:4px;border-left:2px solid #444;border-bottom:2px solid #444;transform:rotate(-45deg)}
.about-btn{left:491px;top:1860px;width:102px;height:37px;line-height:37px;font-size:13px}

/* footer */
.footer{left:0;top:1930px;width:1200px;height:331px;background:var(--footer);color:#fff}
.f-brand{left:82px;top:1968px;width:318px;text-align:center;white-space:nowrap}
.f-brand .n{font-size:25px;letter-spacing:1px;line-height:1.1}
.f-brand .s{font-size:14px;letter-spacing:2px}
.f-rule{left:92px;width:298px;height:1px;background:#666}
.f-addr{left:92px;top:2067px;width:298px;text-align:center;font-size:12px;line-height:20px}
.f-copy{left:92px;top:2192px;width:298px;text-align:center;font-size:12px}
.f-head{font-size:17px;letter-spacing:1px;white-space:nowrap}
.f-menu{left:475px;top:2002px;list-style:none;font-size:12px;line-height:23px}
.f-social{left:626px;top:2002px;list-style:none;font-size:12px}
.f-social li{display:flex;align-items:center;gap:14px;height:36px}
.f-social i{width:22px;height:22px;border-radius:50%;display:block}
.field{left:815px;width:282px;background:var(--field);font-size:12px;color:#ccc;padding:10px 14px}
.submit{left:1015px;top:2184px;width:82px;height:32px;line-height:32px;font-size:13px}
</style>
</head>
<body>

<div class="abs topline"></div>
<div class="abs brand">
  <div class="brand-mark"></div>
  <div class="brand-name serif">BRACKENFOLD LANE</div>
  <div class="brand-sub serif">VINEYARD</div>
</div>
<div class="abs callus">
  <svg width="34" height="34" viewBox="0 0 34 34"><circle cx="17" cy="17" r="15.5" fill="none" stroke="#1e9a33" stroke-width="2"/><path d="M12 10c1-1 2 0 3 2s0 2-1 3c1 2 3 4 5 5 1-1 1-2 3-1s3 2 2 3c-1 2-3 2-5 1-4-2-7-5-8-9-1-2 0-3 1-4z" fill="#1e9a33"/></svg>
  <div><div class="lbl">Call us</div><div class="num">+61 400 555 218</div></div>
</div>
<div class="abs search"><span>Enter your keywords.....</span><b><svg width="16" height="16" viewBox="0 0 16 16"><circle cx="6.5" cy="6.5" r="4.8" fill="none" stroke="#fff" stroke-width="2"/><path d="M10 10l4.5 4.5" stroke="#fff" stroke-width="2.4"/></svg></b></div>

<nav class="abs nav">
  <a class="home" href="#">HOME</a>
  <a href="#" style="left:268px">WINE</a>
  <a href="#" style="left:384px">CONTACT US</a>
  <a href="#" style="left:507px">EVENTS</a>
  <a href="#" style="left:612px">GALLERY</a>
  <a href="#" style="left:716px">ABOUT US</a>
  <a href="#" style="left:817px">CART</a>
  <a href="#" style="left:921px">MEMBERS</a>
  <a href="#" style="left:1037px">OUTLETS</a>
  <span class="sep" style="left:310px"></span><span class="sep" style="left:455px"></span><span class="sep" style="left:560px"></span><span class="sep" style="left:664px"></span><span class="sep" style="left:770px"></span><span class="sep" style="left:866px"></span><span class="sep" style="left:980px"></span><span class="sep" style="left:1098px"></span>
</nav>

<div class="abs hero" role="img" aria-label="Warm sunset vineyard scene with grape cluster, wine bottle, filled wine glass and an oak barrel"></div>
<div class="abs hero-title serif">A LITTLE WAY ALONG THE ROAD</div>
<div class="abs hero-text">A few years ago, a couple decided to follow their dreams and buy a small beautiful vineyard!Daniel was studying viticulture</div>
<div class="abs btn-solid hero-btn">View more</div>
<svg class="abs arrow" style="left:32px" width="20" height="52" viewBox="0 0 20 52"><path d="M18 1L2 26l16 25" fill="none" stroke="#fff" stroke-width="1.5"/></svg>
<svg class="abs arrow" style="left:1146px" width="20" height="52" viewBox="0 0 20 52"><path d="M2 1l16 25L2 51" fill="none" stroke="#fff" stroke-width="1.5"/></svg>

<div class="abs feature" style="left:100px">
  <div class="circle"><svg width="50" height="50" viewBox="0 0 50 50"><path d="M2 8l14-5v40L2 48z M19 3l12 5v40l-12-5z M34 8l14-5v40l-14 5z" fill="#1e9a33"/></svg></div>
  <h3 class="serif">TOUR</h3>
  <p>A few years ago, a couple decided to follow their dreams and buy a small beautiful vineyard!Daniel was studying viticulture and Leah loved drinking wine</p>
  <div class="btn-line">View more</div>
</div>
<div class="abs feature" style="left:440px">
  <div class="circle"><svg width="56" height="42" viewBox="0 0 56 42"><path d="M2 4h32v26H2z M36 12h10l8 10v8H36z" fill="#1e9a33"/><circle cx="12" cy="34" r="6" fill="#1e9a33" stroke="#fff" stroke-width="2"/><circle cx="44" cy="34" r="6" fill="#1e9a33" stroke="#fff" stroke-width="2"/><path d="M40 15h5l5 6h-10z" fill="#fff"/></svg></div>
  <h3 class="serif">FREE SHIPPING</h3>
  <p>A few years ago, a couple decided to follow their dreams and buy a small beautiful vineyard!Daniel was studying viticulture and Leah loved drinking wine</p>
  <div class="btn-line">View more</div>
</div>
<div class="abs feature" style="left:782px">
  <div class="circle"><svg width="46" height="48" viewBox="0 0 46 48"><rect x="2" y="6" width="42" height="40" rx="3" fill="#1e9a33"/><rect x="11" y="1" width="4" height="10" fill="#1e9a33"/><rect x="31" y="1" width="4" height="10" fill="#1e9a33"/><g fill="#fff"><rect x="7" y="16" width="7" height="6"/><rect x="16" y="16" width="7" height="6"/><rect x="25" y="16" width="7" height="6"/><rect x="34" y="16" width="6" height="6"/><rect x="7" y="25" width="7" height="6"/><rect x="16" y="25" width="7" height="6"/><rect x="25" y="25" width="7" height="6"/><rect x="34" y="25" width="6" height="6"/><rect x="7" y="34" width="7" height="6"/><rect x="16" y="34" width="7" height="6"/><rect x="25" y="34" width="7" height="6"/><rect x="34" y="34" width="6" height="6"/></g></svg></div>
  <h3 class="serif">EVENTS</h3>
  <p>A few years ago, a couple decided to follow their dreams and buy a small beautiful vineyard!Daniel was studying viticulture and Leah loved drinking wine</p>
  <div class="btn-line">View more</div>
</div>

<section class="abs products"></section>
<div class="abs prod-head"><h2 class="sec-title serif" style="font-weight:400">OUR PRODUCTS</h2></div>

<div class="abs card" style="left:98px">
  <div class="img"><div class="bottle" role="img" aria-label="Red wine bottle" style="background:linear-gradient(#7a1f1f 0 12%,#2a1a1a 12% 55%,#eee 55% 88%,#2a1a1a 88%)"></div></div>
  <div class="sale">Sale!</div>
  <h4 class="serif">EMBER AND OAK RED 2015</h4><div class="price">$18.18</div>
  <div class="row"><div class="qty">1</div><div class="add">Addcart</div></div>
</div>
<div class="abs card" style="left:353px">
  <div class="img"><div class="bottle" role="img" aria-label="Riesling bottle" style="background:linear-gradient(#e07a1a 0 12%,#8a8a1a 12% 55%,#e08a1a 55% 90%,#6a6a10 90%)"></div></div>
  <h4 class="serif">RIESLING 2015</h4><div class="price">$18.18</div>
  <div class="row"><div class="qty">1</div><div class="add">Addcart</div></div>
</div>
<div class="abs card" style="left:609px">
  <div class="img"><div class="bottle" role="img" aria-label="Sauvignon blanc bottle" style="background:linear-gradient(#eee 0 12%,#3a4a1a 12% 55%,#eee 55% 88%,#3a4a1a 88%)"></div></div>
  <h4 class="serif">SAUVIGNON BLANC 2014</h4><div class="price">$18.18</div>
  <div class="row"><div class="qty">1</div><div class="add">Addcart</div></div>
</div>
<div class="abs card" style="left:864px">
  <div class="img"><div class="bottle" role="img" aria-label="Sauvignon blanc bottle" style="background:linear-gradient(#dde 0 12%,#d8d040 12% 55%,#f4f4f4 55% 88%,#d8d040 88%)"></div></div>
  <h4 class="serif">SAUVIGNON BLANC 2015</h4><div class="price">$18.18</div>
  <div class="row"><div class="qty">1</div><div class="add">Addcart</div></div>
</div>

<div class="abs about-photo" role="img" aria-label="Two staff members at a wine tasting stand holding bottles"></div>
<div class="abs about-head"><h2 class="sec-title serif" style="font-weight:400">ABOUT US</h2></div>
<ul class="abs about-list">
  <li>A few years ago, a couple decided to follow their dreams and buy a small beautiful vineyard!<br>Daniel was studying viticulture and Leah loved drinking wine – a perfect match really!</li>
  <li>To seal the deal, they were to be given (by the previous owners) a big red tractor and a black dog the rest is history!</li>
  <li>Brackenfold Lane Vineyard is the start of a dream, a life long passion to live on the land and to produce award-winning wine. And a place they can welcome guests to experience what a vineyard is all about (and tasting wine)!</li>
  <li>Three years later, they have achieved this and added to the family of more children and more dogs!<br>So please, join them on the journey....</li>
</ul>
<div class="abs btn-solid about-btn">Read more</div>

<footer class="abs footer"></footer>
<div class="abs f-brand serif" style="color:#fff"><div class="n">BRACKENFOLD LANE</div><div class="s">VINEYARD</div></div>
<div class="abs f-rule" style="top:2053px"></div>
<div class="abs f-addr" style="color:#fff">12 Brackenfold Lane · Marrowvale<br>NSW · 2600 · Australia<br>T : +61 400 555 218<br>E : wine@brackenfoldlane.com.au</div>
<div class="abs f-rule" style="top:2168px"></div>
<div class="abs f-copy" style="color:#fff">Copyrights @2016 All Rights Reserved</div>

<div class="abs f-head serif" style="left:475px;top:1970px;color:#fff">MENU</div>
<ul class="abs f-menu" style="color:#fff"><li>Home</li><li>Wine</li><li>Contact us</li><li>Events</li><li>Gallery</li><li>About us</li><li>Cart</li><li>Members</li><li>outlets</li></ul>

<div class="abs f-head serif" style="left:626px;top:1970px;color:#fff">FOLLOW US ON</div>
<ul class="abs f-social" style="color:#fff">
  <li><i style="background:#3b5998"></i>Community</li>
  <li><i style="background:#1da1f2"></i>Updates</li>
  <li><i style="background:#0e76a8"></i>Network</li>
  <li><i style="background:#f26522"></i>RSS Feed</li>
</ul>

<div class="abs f-head serif" style="left:811px;top:1970px;color:#fff">QUICK CONTACT</div>
<div class="abs field" style="top:2008px;height:36px">Enter your name...</div>
<div class="abs field" style="top:2049px;height:36px">E-mail address...</div>
<div class="abs field" style="top:2091px;height:86px">Message...</div>
<div class="abs btn-solid submit">Submit</div>

</body>
</html>
```